Business Card Design - Trelvo Services

Trelvo Services is a service company which carried out installation and maintenance work in the GPS Tracking industry.

We install and maintain GPS Tracking hardware into cars, trucks etc.

We have an existing design with existing logo which I would like to improve on. I would like to be able to edit the design in the future when we have new staff come on board. We currently have 8 or so different employees who would all require cards - ideally I need to be able to edit a template in photoshop or something.

The back of the existing design has a white outline of Australia with a white dot over: Brisbane, Sydney, Melbourne, Adelaide and Perth.

Our current cards are mainly black, our uniforms are black - happy to look at changing that if the look is right.

We strive to be organised, professional and we are working in the technology sector.

Cheers.

Industry/Entity Type

Business

Contact Information for Business Card

Name
Mobile number
Email address
Web address

Requirements
Must have
• Map of Australia as mentioned above.

```html
<!DOCTYPE html>
<html lang="en">
<head>
<meta charset="utf-8">
<title>Trelvo Services – Business Card</title>
<link rel="stylesheet" href="https://fonts.googleapis.com/css2?family=Jost:wght@400;600;700&display=swap">
<style>
  :root {
    --stage: #1e1e1e;
    --card: #050505;
    --card-edge: #161616;
    --accent: #3a7fc8;
    --text: #f2f2f2;
    --rule: #5a5a5a;
    --map-tone-a: #141414;
    --map-tone-b: #0b0b0b;
  }
  * { box-sizing: border-box; margin: 0; padding: 0; }
  html, body {
    width: 1200px; height: 871px; overflow: hidden;
    background: var(--stage);
    font-family: "Jost", "Futura", sans-serif;
  }
  .sheet {
    width: 1200px; height: 871px;
    display: flex; flex-direction: column; align-items: center; justify-content: center;
    gap: 44px;
  }
  .card {
    position: relative;
    width: 580px; height: 354px;
    background: var(--card);
    border: 1px solid var(--card-edge);
    box-shadow: 0 18px 40px rgba(0,0,0,.55);
    overflow: hidden;
  }

  /* Back */
  .card-back__map {
    position: absolute; left: 150px; top: 22px; width: 400px; height: 250px;
    background: radial-gradient(ellipse at 55% 50%, var(--map-tone-a), var(--map-tone-b) 75%);
    border-radius: 40% 45% 38% 50%;
  }
  .card-back__name {
    position: absolute; left: 34px; bottom: 34px;
    font-weight: 700; font-size: 30px; letter-spacing: -0.5px;
    color: var(--accent);
  }

  /* Front */
  .card-front__band {
    position: absolute; left: 0; top: 0; bottom: 0; width: 34px;
    background: var(--accent);
  }
  .card-front__tab {
    position: absolute; left: 0; top: 142px; width: 52px; height: 104px;
    background: var(--accent);
    border-radius: 0 10px 10px 0;
    display: flex; flex-direction: column; justify-content: space-between; align-items: center;
    padding: 10px 0 10px 14px;
  }
  .card-front__tab svg { width: 16px; height: 16px; }
  .card-front__logo {
    position: absolute; right: 40px; top: 72px;
    font-weight: 700; font-size: 34px; letter-spacing: -0.5px;
    color: var(--text);
  }
  .card-front__person {
    position: absolute; left: 86px; top: 104px;
    font-weight: 600; font-size: 19px; letter-spacing: 1.5px;
    color: var(--text);
  }
  .card-front__rule {
    position: absolute; left: 86px; right: 0; top: 136px;
    height: 1px; background: var(--rule);
  }
  .card-front__contacts {
    position: absolute; left: 86px; top: 150px;
    list-style: none;
    font-size: 15px; line-height: 25px; letter-spacing: 1.6px;
    color: var(--text);
  }
</style>
</head>
<body>
<main class="sheet">

  <section class="card card-back" aria-label="Card back">
    <div class="card-back__map" role="img" aria-label="Outline map of Australia with dots over Brisbane, Sydney, Melbourne, Adelaide and Perth"></div>
    <p class="card-back__name">Trelvo Services</p>
  </section>

  <section class="card card-front" aria-label="Card front">
    <div class="card-front__band"></div>
    <div class="card-front__tab">
      <svg viewBox="0 0 16 16" fill="none" stroke="#fff" stroke-width="1.3" aria-label="Mobile">
        <path d="M4 2h3l1 3-2 1.5c.8 1.8 2 3 3.5 3.5L11 8l3 1v3c0 1-1 2-2 2C6.5 14 2 9.5 2 4c0-1 1-2 2-2z"/>
      </svg>
      <svg viewBox="0 0 16 16" fill="none" stroke="#fff" stroke-width="1.3" aria-label="Phone">
        <rect x="4" y="2" width="8" height="4"/><rect x="2" y="6" width="12" height="6" rx="1"/><rect x="4.5" y="10" width="7" height="4"/>
      </svg>
      <svg viewBox="0 0 16 16" fill="none" stroke="#fff" stroke-width="1.3" aria-label="Email">
        <rect x="1.5" y="3.5" width="13" height="9"/><path d="M1.5 3.5 8 9l6.5-5.5"/>
      </svg>
      <svg viewBox="0 0 16 16" fill="none" stroke="#fff" stroke-width="1.3" aria-label="Web">
        <circle cx="8" cy="8" r="6.3"/><ellipse cx="8" cy="8" rx="2.8" ry="6.3"/><path d="M1.7 8h12.6M2.8 4.8h10.4M2.8 11.2h10.4"/>
      </svg>
    </div>

    <p class="card-front__logo">Trelvo Services</p>
    <h1 class="card-front__person">Daniel Marsh</h1>
    <div class="card-front__rule"></div>
    <ul class="card-front__contacts">
      <li>0400 555 218</li>
      <li>(07) 3000 4127</li>
      <li>daniel@trelvoservices.com.au</li>
      <li>www.trelvoservices.com.au</li>
    </ul>
  </section>

</main>
</body>
</html>
```